Professional and modern website for Real Estate services company

Hi there! We're looking for a responsive, highly professional and modern (in line with Latest trends) coded website for a Real Estate services company named Portalia (find logo attached). I will try to Explain how I picture it in my head, but feel free to step out of the script and design it as you please. The structure for the website must be as Follows: - Menu: at the top of the screen, always visible (in any page and when to scrolling down). Logo at the left hand side (clicking redirects to home), then a Services, About us, Blog and Contact and on the right hand, Estimate and Log in (just placeholder, no log in required yet). - Home: (I like https://fr.domvera.example/): a landscape picture of Madrid's skyline. Very important That at a first glance (without scrolling) you can see a box to input data of your building to get an estimate (Post code, Number of homes, Number of garages, Number of stores, Swimming pool (yes / no) Concierge (yes / no)). Should there be a small space Also for a corporate presentation video (more or less like https://www.velbrastahogares.example/ but With the estimate Request box INSTEAD OF the App - however, do not take this one as example Given I just wanted to illustrate the structure). Still in the Home, bellow the first glance, I'd like to have a brief introduction of the following pages (Services, About us, Blog and Contact). This can be in a Either "square" form (like https://fr.domvera.example/) or in a "scroll" form (like https://k7pisos.example/). - Services: we offer 3 sets of services, each of them composed by three specific services, Namely: * Administration Treasury Accounting Savings * Consulting Legal Technical Regulatory * Mediation Repairs Meetings Delinquency For the sake of structuring, each of the nine services will Have to written description composed of 3 small paragraphs of About 15 words. I Tend to like to Accompany With each of the services related icons / vectors, but feel free to design them as you want. - About us: content not yet defined, but will be a series of bullets / sections in Which We talk about prep or differentiating points. We can include the corporate video presentation here again. - Blog: just a space Where you can see to the blog entries (in Home, probably just show 3/4). - Contact: a fancy contact form, with map, address, telephone, e-mail and opening hours. Just to give it a bit more content, maybe include a catch phrase like "We're looking forward to meeting you!" or something like that. - Estimate: this is the Most Important page in the website (in Addition to the upper part of the Home page). Basically replicate the estimate for the home box, but maybe with a bit more design or extended, Given this is a single page just for that. - Log in: opens a drop-down with user and password (just placeholder, no log in required yet). Regarding colors, we still do not Have a color scheme, so anything in line With the logo is OK. Many thanks in advance, Martin

All ages and genders

Real Estate

Coded - Design and coding required

5+ page

Sans Serif

Must have
• Blank colored background

```html
<!DOCTYPE html>
<html lang="en">
<head>
<meta charset="utf-8">
<title>Portalia — A Tradition Of Trust</title>
<link href="https://fonts.googleapis.com/css2?family=Roboto:wght@300;400;500;700&display=swap" rel="stylesheet">
<style>
:root{
  --orange:#e8821e;
  --orange-dark:#c96a10;
  --ink:#222;
  --text:#555;
  --muted:#888;
  --grey-band:#ececec;
  --footer:#2b2520;
  --white:#fff;
}
*{box-sizing:border-box;margin:0;padding:0}
html,body{width:1200px;height:5042px;overflow:hidden}
body{font-family:'Roboto',Arial,sans-serif;color:var(--text);background:var(--white);font-size:14px}
a{color:inherit;text-decoration:none}

.site-header{height:94px;display:flex;align-items:center;justify-content:space-between;padding:0 70px 0 80px;background:var(--white)}
.brand{display:flex;align-items:center;gap:10px;font-size:30px;font-weight:700;color:var(--ink)}
.brand-mark{width:14px;height:14px;background:var(--orange)}
.main-nav{display:flex;align-items:center;gap:24px;font-size:15px;color:#444}
.main-nav .active{color:var(--orange)}
.btn-login{background:var(--orange);color:#fff;padding:8px 16px}
.btn-estimate{background:#555;color:#fff;padding:8px 16px}

.hero{position:relative;height:612px;background:linear-gradient(180deg,#e07a2a 0%,#b45322 40%,#4a2a22 75%,#1e1a1c 100%)}
.hero-title{position:absolute;left:80px;top:270px;color:#fff}
.hero-title .name{font-size:42px;font-weight:700}
.hero-title .tagline{font-size:58px;font-weight:500;margin-top:6px}
.estimate-box{position:absolute;left:772px;top:60px;width:325px;height:500px;background:rgba(20,20,20,.78);padding:22px 28px}
.estimate-box h2{color:var(--orange);font-size:22px;font-weight:400;text-align:center}
.estimate-box .sub{color:#ddd;font-size:12px;text-align:center;border-bottom:1px solid #666;padding-bottom:10px;margin-bottom:14px}
.field{height:30px;background:#fff;margin-bottom:12px;display:flex;align-items:center;gap:8px;padding:0 10px;font-size:12px;color:#666}
.field i{width:10px;height:10px;border:1.5px solid #777;border-radius:2px}
.yesno{display:flex;justify-content:space-between;color:#fff;font-size:12px;margin:6px 0 10px}
.yesno span b{display:inline-block;width:9px;height:9px;background:#fff;margin:0 4px 0 6px;border-radius:50%}
.submit{display:block;margin:14px auto 0;width:190px;height:36px;background:var(--orange);color:#fff;text-align:center;line-height:36px;font-size:15px}

.about{height:393px;display:flex;gap:40px;padding:50px 80px 0}
.about-text{width:620px}
.about h2{font-size:30px;color:var(--ink);font-weight:700;margin-bottom:16px}
.about h2 span{color:var(--orange)}
.about p{font-size:12.5px;line-height:1.7;margin-bottom:14px}
.about-video{width:340px;height:230px;margin-left:auto;margin-top:40px;background:linear-gradient(135deg,#d9dde3,#7b8796)}

.banner{position:relative;display:flex;flex-direction:column;align-items:center;justify-content:center;color:#fff;text-align:center;padding:0 60px}
.banner h2{font-size:40px;font-weight:500;margin-bottom:22px}
.banner p{font-size:15px;line-height:1.7;max-width:1100px}
.banner-admin{height:504px;background:linear-gradient(180deg,#2e3a40,#4a5a60 60%,#263036)}
.banner-consult{height:494px;background:linear-gradient(120deg,#f0a040,#e8821e 50%,#f5b560);color:#222}
.banner-consult h2{color:#222}
.banner-mediation{height:504px;background:linear-gradient(180deg,#3a3a3c,#5a5a5e 50%,#242426)}
.notch{position:absolute;bottom:-22px;left:50%;margin-left:-24px;width:0;height:0;border-left:24px solid transparent;border-right:24px solid transparent;border-top:22px solid #263036;z-index:2}
.banner-mediation .notch{border-top-color:#242426}

.services{display:flex;justify-content:space-around;padding:60px 120px 0}
.services-admin{height:407px}
.services-consult{height:420px}
.services-mediation{height:414px}
.service{width:250px;text-align:center}
.service-icon{width:120px;height:120px;border:3px solid var(--orange);border-radius:50%;margin:0 auto 20px;display:flex;align-items:center;justify-content:center}
.service h3{font-size:20px;font-weight:400;color:var(--ink);margin-bottom:10px}
.service p{font-size:11.5px;line-height:1.6;color:var(--muted)}
.read-more{display:inline-block;margin-top:12px;color:var(--orange);font-size:12px}

.testimonials{height:343px;background:var(--grey-band);padding-top:60px}
.section-title{text-align:center;font-size:30px;font-weight:700;color:var(--ink)}
.section-title span{color:var(--orange)}
.quotes{display:flex;justify-content:center;gap:90px;margin-top:50px}
.quote{display:flex;align-items:center;gap:24px;width:420px}
.avatar{width:120px;height:120px;border-radius:50%;border:4px solid var(--orange);background:linear-gradient(135deg,#c9b8a8,#7d6a5c);flex:none}
.quote-mark{color:var(--orange);font-size:48px;font-weight:700;line-height:.5}
.quote p{font-size:13px;font-weight:700;color:#333;line-height:1.5}
.quote .who{color:var(--orange);font-size:12px;font-weight:400;margin-top:8px}

.blog{height:548px;padding-top:50px}
.posts{display:flex;justify-content:center;gap:44px;margin-top:40px}
.post{width:340px;text-align:center}
.post-image{position:relative;height:270px}
.post-date{position:absolute;left:0;top:0;width:60px;height:60px;background:var(--orange);color:#fff;text-align:center;font-size:20px;font-weight:700;padding-top:8px}
.post-date small{display:block;font-size:11px;font-weight:400}
.post h3{font-size:18px;font-weight:400;color:var(--ink);margin:20px 0 12px}
.post p{font-size:11.5px;line-height:1.6;color:var(--muted)}
.img-city{background:linear-gradient(180deg,#f2a24a,#8a4a20)}
.img-tower{background:linear-gradient(135deg,#f1c27a,#c07a28 60%,#6a3a18)}
.img-glass{background:linear-gradient(180deg,#3a7ac8,#9ab8d8 60%,#3c4a5a)}

.site-footer{height:309px;background:var(--footer);color:#ddd;position:relative}
.footer-cols{display:flex;gap:70px;padding:46px 80px 0}
.footer-cols h4{color:var(--orange);font-size:18px;font-weight:400;margin-bottom:14px}
.footer-cols li{list-style:none;font-size:13px;line-height:1.75}
.col-links{width:200px}
.col-news{width:260px}
.col-social{width:220px}
.newsletter-input{width:210px;height:34px;background:#fff;border-radius:18px;font-size:12px;color:#777;line-height:34px;padding-left:16px}
.newsletter-btn{width:100px;height:32px;background:var(--orange);border-radius:16px;color:#fff;text-align:center;line-height:32px;margin-top:12px;font-size:13px}
.socials{display:flex;gap:14px}
.socials span{width:34px;height:34px;border-radius:50%;background:#fff}
.copyright{position:absolute;bottom:0;left:0;right:0;height:40px;background:var(--orange);color:#fff;text-align:center;line-height:40px;font-size:12px}
</style>
</head>
<body>

<header class="site-header">
  <a class="brand" href="#"><span class="brand-mark"></span>Portalia</a>
  <nav class="main-nav">
    <a class="active" href="#">Home</a><a href="#">About Us</a><a href="#">Our services</a><a href="#">Blog</a><a href="#">Contact</a>
    <a class="btn-login" href="#">Log in</a><a class="btn-estimate" href="#">Estimate</a>
  </nav>
</header>

<section class="hero" role="img" aria-label="Madrid skyline at sunset">
  <div class="hero-title"><div class="name">Portalia</div><div class="tagline">A Tradition Of Trust.</div></div>
  <form class="estimate-box">
    <h2>Get A Free Estimate</h2>
    <p class="sub">Tell Us About Your Requirement</p>
    <div class="field"><i></i>Name</div>
    <div class="field"><i></i>Email Id</div>
    <div class="field"><i></i>Post Code</div>
    <div class="field"><i></i>Number Of Homes</div>
    <div class="field"><i></i>Number Of Garages</div>
    <div class="field"><i></i>Number Of Stores</div>
    <div class="yesno"><span>Swimming Pool</span><span><b></b>Yes<b></b>No</span></div>
    <div class="yesno"><span>Concierge</span><span><b></b>Yes<b></b>No</span></div>
    <span class="submit">Submit Now</span>
  </form>
</section>

<section class="about">
  <div class="about-text">
    <h2>About <span>Portalia</span></h2>
    <p>Lorem ipsum dolor sit amet, consectetur adipiscing elit. Morbi eu ligula sit amet elit consectetur iaculis sit amet eu velit. Sed tempus leo felis, quis mollis velit euismod sed. Fusce porttitor sagittis est. Nam consectetur porta euismod. Nulla rhoncus, nisi non efficitur lacinia, metus risus efficitur lacus, sit amet ornare magna tellus volutpat mi. Quisque scelerisque dui non tincidunt tempor.</p>
    <p>Cras egestas lectus urna, quis interdum nulla aliquam eu. Vestibulum lobortis sem sed tortor lacinia, at aliquet turpis hendrerit. Curabitur tempus non risus nec dictum. Mauris vel pharetra sapien, a consectetur velit. In hac habitasse platea dictumst. In odio metus, scelerisque ac odio id, lobortis porttitor turpis. Fusce vel diam quis nunc dignissim dignissim nec et sem. Nulla ut ligula tristique.</p>
  </div>
  <div class="about-video" role="img" aria-label="Corporate presentation video: handshake"></div>
</section>

<section class="banner banner-admin" role="img" aria-label="City skyline from above">
  <h2>Administration</h2>
  <p>Lorem ipsum dolor sit amet, consectetur adipiscing elit. Duis mollis lorem ut urna accumsan sagittis. Etiam a dui eu diam malesuada consectetur. Sed ac ullamcorper nunc. Integer bibendum egestas lobortis. Suspendisse aliquam consequat nisl sit amet mattis. Etiam pretium eros massa, eu rhoncus mauris vehicula eu. Nulla et velit odio. Duis ipsum sem, molestie cursus quam at, sodales feugiat mi.</p>
  <span class="notch"></span>
</section>

<section class="services services-admin">
  <div class="service">
    <div class="service-icon"><svg width="60" height="60" viewBox="0 0 60 60" fill="none" stroke="#e8821e" stroke-width="3"><path d="M8 22 30 10l22 12z"/><path d="M14 26v20M24 26v20M36 26v20M46 26v20M8 50h44"/></svg></div>
    <h3>Treasury</h3><p>Nullam euismod feugiat turpis in sollicitudin. Donec a tortor mattis, blandit leo at, volutpat ex. Pellentesque habitant morbi tristique senectus et netus.</p><a class="read-more" href="#">Read More&gt;&gt;</a>
  </div>
  <div class="service">
    <div class="service-icon"><svg width="60" height="60" viewBox="0 0 60 60" fill="none" stroke="#e8821e" stroke-width="3"><rect x="14" y="8" width="32" height="44" rx="3"/><rect x="19" y="13" width="22" height="9"/><path d="M20 30h4M28 30h4M36 30h4M20 38h4M28 38h4M36 38h4M20 46h4M28 46h4M36 46h4"/></svg></div>
    <h3>Accounting</h3><p>Nullam euismod feugiat turpis in sollicitudin. Donec a tortor mattis, blandit leo at, volutpat ex. Pellentesque habitant morbi tristique senectus et netus.</p><a class="read-more" href="#">Read More&gt;&gt;</a>
  </div>
  <div class="service">
    <div class="service-icon"><svg width="60" height="60" viewBox="0 0 60 60" fill="none" stroke="#e8821e" stroke-width="3"><ellipse cx="30" cy="34" rx="20" ry="14"/><circle cx="30" cy="14" r="6"/><path d="M22 46v6M38 46v6"/></svg></div>
    <h3>Savings</h3><p>Nullam euismod feugiat turpis in sollicitudin. Donec a tortor mattis, blandit leo at, volutpat ex. Pellentesque habitant morbi tristique senectus et netus.</p><a class="read-more" href="#">Read More&gt;&gt;</a>
  </div>
</section>

<section class="banner banner-consult" role="img" aria-label="Consultants reviewing documents together">
  <h2>Consulting</h2>
  <p>Lorem ipsum dolor sit amet, consectetur adipiscing elit. Duis mollis lorem ut urna accumsan sagittis. Etiam a dui eu diam malesuada consectetur. Sed ac ullamcorper nunc. Integer bibendum egestas lobortis. Suspendisse aliquam consequat nisl sit amet mattis. Etiam pretium eros massa, eu rhoncus mauris vehicula eu. Nulla et velit odio. Duis ipsum sem, molestie cursus quam at, sodales feugiat mi.</p>
</section>

<section class="services services-consult">
  <div class="service">
    <div class="service-icon"><svg width="60" height="60" viewBox="0 0 60 60" fill="none" stroke="#e8821e" stroke-width="3"><path d="M18 14l14 14M26 8l12 12M14 20l10-10M32 22 20 34"/><path d="M30 26l18 18"/><path d="M10 52h26"/></svg></div>
    <h3>Legal</h3><p>Nullam euismod feugiat turpis in sollicitudin. Donec a tortor mattis, blandit leo at, volutpat ex. Pellentesque habitant morbi tristique senectus et netus.</p><a class="read-more" href="#">Read More&gt;&gt;</a>
  </div>
  <div class="service">
    <div class="service-icon"><svg width="60" height="60" viewBox="0 0 60 60" fill="none" stroke="#e8821e" stroke-width="3"><circle cx="24" cy="34" r="12"/><circle cx="24" cy="34" r="4"/><circle cx="42" cy="18" r="8"/><circle cx="42" cy="18" r="2"/></svg></div>
    <h3>Technical</h3><p>Nullam euismod feugiat turpis in sollicitudin. Donec a tortor mattis, blandit leo at, volutpat ex. Pellentesque habitant morbi tristique senectus et netus.</p><a class="read-more" href="#">Read More&gt;&gt;</a>
  </div>
  <div class="service">
    <div class="service-icon"><svg width="60" height="60" viewBox="0 0 60 60" fill="none" stroke="#e8821e" stroke-width="3"><rect x="14" y="8" width="32" height="44"/><path d="M20 18h20M20 26h20M20 34h14"/><circle cx="38" cy="44" r="5"/></svg></div>
    <h3>Regulatory</h3><p>Nullam euismod feugiat turpis in sollicitudin. Donec a tortor mattis, blandit leo at, volutpat ex. Pellentesque habitant morbi tristique senectus et netus.</p><a class="read-more" href="#">Read More&gt;&gt;</a>
  </div>
</section>

<section class="banner banner-mediation" role="img" aria-label="Model house on a calculator">
  <h2>Mediation</h2>
  <p>Lorem ipsum dolor sit amet, consectetur adipiscing elit. Duis mollis lorem ut urna accumsan sagittis. Etiam a dui eu diam malesuada consectetur. Sed ac ullamcorper nunc. Integer bibendum egestas lobortis. Suspendisse aliquam consequat nisl sit amet mattis. Etiam pretium eros massa, eu rhoncus mauris vehicula eu. Nulla et velit odio. Duis ipsum sem, molestie cursus quam at, sodales feugiat mi.</p>
  <span class="notch"></span>
</section>

<section class="services services-mediation">
  <div class="service">
    <div class="service-icon"><svg width="60" height="60" viewBox="0 0 60 60" fill="none" stroke="#e8821e" stroke-width="3"><path d="M14 14l32 32M46 14 14 46"/><circle cx="14" cy="14" r="5"/><circle cx="46" cy="46" r="4"/></svg></div>
    <h3>Repairs</h3><p>Nullam euismod feugiat turpis in sollicitudin. Donec a tortor mattis, blandit leo at, volutpat ex. Pellentesque habitant morbi tristique senectus et netus.</p><a class="read-more" href="#">Read More&gt;&gt;</a>
  </div>
  <div class="service">
    <div class="service-icon"><svg width="60" height="60" viewBox="0 0 60 60" fill="none" stroke="#e8821e" stroke-width="3"><rect x="10" y="28" width="40" height="8"/><circle cx="18" cy="18" r="4"/><circle cx="30" cy="16" r="4"/><circle cx="42" cy="18" r="4"/><path d="M16 36v12M44 36v12"/></svg></div>
    <h3>Meetings</h3><p>Nullam euismod feugiat turpis in sollicitudin. Donec a tortor mattis, blandit leo at, volutpat ex. Pellentesque habitant morbi tristique senectus et netus.</p><a class="read-more" href="#">Read More&gt;&gt;</a>
  </div>
  <div class="service">
    <div class="service-icon"><svg width="60" height="60" viewBox="0 0 60 60" fill="none" stroke="#e8821e" stroke-width="3"><rect x="14" y="8" width="32" height="44"/><path d="M20 18h20M20 26h20M20 34h20M20 42h10"/></svg></div>
    <h3>Delinquency</h3><p>Nullam euismod feugiat turpis in sollicitudin. Donec a tortor mattis, blandit leo at, volutpat ex. Pellentesque habitant morbi tristique senectus et netus.</p><a class="read-more" href="#">Read More&gt;&gt;</a>
  </div>
</section>

<section class="testimonials">
  <h2 class="section-title">Client's <span>Testimonials</span></h2>
  <div class="quotes">
    <div class="quote"><div class="avatar" role="img" aria-label="Client portrait"></div><div><div class="quote-mark">“</div><p>Lorem ipsum dolor sit amet, consectetur adipiscing elit. Maecenas venenatis ultrices tincidunt.</p><div class="who">- Ines Marlowe</div></div></div>
    <div class="quote"><div class="avatar" role="img" aria-label="Client portrait"></div><div><div class="quote-mark">“</div><p>Lorem ipsum dolor sit amet, consectetur adipiscing elit. Maecenas venenatis ultrices tincidunt.</p><div class="who">- Laura Pell</div></div></div>
  </div>
</section>

<section class="blog">
  <h2 class="section-title">Recent <span>Blog Post</span></h2>
  <div class="posts">
    <article class="post"><div class="post-image img-city" role="img" aria-label="City aerial view at dusk"><div class="post-date">28<small>April</small></div></div><h3>Proin diam purus, posuere nec elit.</h3><p>Nulla ac neque pharetra, elementum erat in, finibus erat. Curabitur in odio in risus fermentum cursus. Morbi non efficitur orci.</p><a class="read-more" href="#">Read More&gt;&gt;</a></article>
    <article class="post"><div class="post-image img-tower" role="img" aria-label="Office tower in sunlight"><div class="post-date">14<small>June</small></div></div><h3>Donec tincidunt pharetra feugiat.</h3><p>Nulla ac neque pharetra, elementum erat in, finibus erat. Curabitur in odio in risus fermentum cursus. Morbi non efficitur orci.</p><a class="read-more" href="#">Read More&gt;&gt;</a></article>
    <article class="post"><div class="post-image img-glass" role="img" aria-label="Modern glass apartment building"><div class="post-date">25<small>October</small></div></div><h3>Cras velmagna pretium posuere nibh.</h3><p>Nulla ac neque pharetra, elementum erat in, finibus erat. Curabitur in odio in risus fermentum cursus. Morbi non efficitur orci.</p><a class="read-more" href="#">Read More&gt;&gt;</a></article>
  </div>
</section>

<footer class="site-footer">
  <div class="footer-cols">
    <div class="col-links"><h4>Quick Links</h4><ul><li>Home</li><li>About Us</li><li>Our services</li><li>Blog</li><li>Contact</li></ul></div>
    <div class="col-news"><h4>Subscribe Our Newsletter</h4><div class="newsletter-input">Enter your email here</div><div class="newsletter-btn">Submit</div></div>
    <div class="col-social"><h4>Social With Us</h4><div class="socials"><span></span><span></span><span></span></div></div>
    <div><h4>Contact Us</h4><ul><li>vip@portalia720.example</li><li>1 (800) 555-0142</li><li>www.portalia720.example</li></ul></div>
  </div>
  <div class="copyright">Copyright 2016 portalia720.example. All rights are reserved.</div>
</footer>

</body>
</html>
```